Spiritual Self Help Book Cover

I need a book cover that's extremely appealing to spiritual seekers, self-help/health and wellness fans. Mostly for women.
The book blends spirituality/mysticism with science for readers to understand how to optimize their health/body, emotional well-being, mental wellness, spiritual fulfillment, relationships, business and purpose in life. It infuses ancient and modern understanding of energy/frequency/quantum mechanics along with the science of chiropractic and psychology.
Book title: Weaving The Silver River
I'll attach some examples that are similar to what I like but I want something different and more extravagantly beautiful.
Please use the graphic of the Sri Yantra Mandala into the cover instead of this stock image one.
I'll need the book cover in all formats: paperback, hardcover, ebook and audiobook.
I'll provide the rest of the details, including publisher logo, synopsis, author photo/blurb and ISBN after I pick the final wniner.
Mostly women spiritual seekers, self-help readers, health/wellness enthusiasts

```html
<!DOCTYPE html>
<html lang="en">
<head>
<meta charset="UTF-8">
<title>Weaving The Silver River — Book Cover</title>
<link href="https://fonts.googleapis.com/css2?family=Montserrat:wght@400;500;700&family=Bebas+Neue&display=swap" rel="stylesheet">
<style>
  :root {
    --ink: #1b3849;
    --gold-light: #f3d07e;
    --gold: #d49c26;
    --gold-deep: #c98f14;
    --lilac: #b9a6ec;
    --pink: #e7a9e6;
    --blush: #efc6e8;
    --aqua: #a9dfe9;
    --mandala-warm: #f6b3a6;
    --mandala-pink: #e98ccf;
    --mandala-violet: #b48ce0;
  }
  * { margin: 0; padding: 0; box-sizing: border-box; }
  html, body {
    width: 849px;
    height: 1200px;
    overflow: hidden;
  }
  body { background: #ffffff; }
  .cover {
    position: relative;
    width: 849px;
    height: 1200px;
    overflow: hidden;
    background:
      radial-gradient(ellipse 320px 420px at 830px 560px, rgba(169, 223, 233, 0.95), rgba(169, 223, 233, 0) 70%),
      radial-gradient(ellipse 460px 300px at 300px 60px, rgba(185, 166, 236, 0.95), rgba(185, 166, 236, 0) 75%),
      radial-gradient(ellipse 380px 360px at 60px 380px, rgba(229, 150, 226, 0.85), rgba(229, 150, 226, 0) 75%),
      linear-gradient(180deg, var(--lilac) 0%, var(--pink) 40%, var(--blush) 75%, #edd0ea 100%);
  }
  .title {
    position: absolute;
    left: 0;
    width: 100%;
    text-align: center;
    white-space: nowrap;
  }
  .title-lead {
    top: 138px;
    font-family: "Montserrat", sans-serif;
    font-weight: 700;
    font-size: 66px;
    line-height: 1;
    letter-spacing: 9px;
    color: var(--ink);
    padding-left: 9px;
  }
  .gold {
    background: linear-gradient(100deg, var(--gold-light) 0%, var(--gold) 22%, var(--gold-deep) 60%, var(--gold) 85%, #e2b95a 100%);
    -webkit-background-clip: text;
    background-clip: text;
    color: transparent;
  }
  .title-middle {
    top: 224px;
    font-family: "Bebas Neue", sans-serif;
    font-size: 146px;
    line-height: 1;
    letter-spacing: 44px;
    padding-left: 44px;
  }
  .title-main {
    top: 340px;
    font-family: "Montserrat", sans-serif;
    font-weight: 700;
    font-size: 212px;
    line-height: 1;
    letter-spacing: -2px;
  }
  .mandala {
    position: absolute;
    left: 128px;
    top: 546px;
    width: 570px;
    height: 492px;
    border-radius: 50%;
    background: radial-gradient(circle at 50% 50%,
      rgba(246, 220, 140, 0.9) 0%,
      rgba(246, 179, 166, 0.85) 25%,
      rgba(233, 140, 207, 0.7) 50%,
      rgba(180, 140, 224, 0.45) 72%,
      rgba(169, 223, 233, 0) 100%);
  }
  .author {
    position: absolute;
    top: 1066px;
    left: 0;
    width: 100%;
    text-align: center;
    font-family: "Montserrat", sans-serif;
    font-weight: 500;
    font-size: 29px;
    line-height: 1;
    letter-spacing: 13px;
    padding-left: 13px;
    color: var(--ink);
    white-space: nowrap;
  }
</style>
</head>
<body>
  <main class="cover">
    <h1 class="book-title">
      <span class="title title-lead">WEAVING THE</span>
      <span class="title title-middle gold">SILVER</span>
      <span class="title title-main gold">RIVER</span>
    </h1>
    <div class="mandala" role="img" aria-label="Rainbow line-art mandala in violet, pink, orange and green"></div>
    <p class="author">DR. MIRIAM HALLOWAY</p>
  </main>
</body>
</html>
```